Web Design Project

We have screen protector brand for mobile phone and we need
Looking for talented web designer. We need only graphic design of 3 page design Home, Catalog page and Product page

- Home page
- There will be rotating banners on the home page
- Top menu will have Hot products, Screen Protectors, Videos, Contact us
- Screen Protectors will be submenu
- Website will be two languages so put US and Turkish flags on the corner so users will be able to switch
- Home page, there will be newest products and hot products and also one video

I also live any additional creative idea for the website
There will be one inner page and catalog page

Check existing page www.durvelo.com which looks pretty bad. You can take logo from there. If you need logo separate i can send it.

I have attached the layout but feel free to change it. I only try to give idea what i wanna see on it.

```html
<!DOCTYPE html>
<html lang="en">
<head>
<meta charset="utf-8">
<title>Durvelo – Screen Protectors</title>
<link href="https://fonts.googleapis.com/css2?family=Oswald:wght@400;500&family=Roboto+Condensed:wght@400&family=Arimo:wght@400&display=swap" rel="stylesheet">
<style>
:root{
  --dark:#36434c;
  --ink:#3a4148;
  --orange:#e8500e;
  --text:#555b60;
  --muted:#6f7478;
  --line:#dcdcdc;
  --panel:#f3f3f3;
  --menu:#ececec;
}
*{margin:0;padding:0;box-sizing:border-box}
html,body{width:819px;height:1200px;overflow:hidden;background:#fff;font-family:Arimo,Arial,sans-serif;color:var(--text)}
.page{position:relative;width:819px;height:1200px}
.abs{position:absolute}
.topbar{left:0;top:0;width:819px;height:31px;background:var(--dark)}
.lang-label{left:632px;top:9px;font-size:10.5px;color:#fff}
.flag{top:4px;width:37px;height:22px}
.flag-us{left:720px}
.flag-tr{left:763px}
.brand{left:35px;top:74px;display:flex;align-items:center;gap:8px;font-family:Oswald,sans-serif;font-weight:500;font-size:29px;letter-spacing:1px;color:var(--ink)}
.brand-mark{width:14px;height:14px;background:var(--ink)}
.nav{left:318px;top:76px;width:420px;height:32px;background:var(--orange);border-radius:4px;display:flex}
.nav a{display:flex;align-items:center;justify-content:center;color:#fff;text-decoration:none;font-family:"Roboto Condensed",sans-serif;font-size:12.5px;border-right:1px solid rgba(255,255,255,.35)}
.nav a:last-child{border-right:none}
.submenu{left:444px;top:110px;width:149px;height:107px;background:var(--menu);border-radius:0 0 4px 4px;padding-top:2px}
.submenu a{display:block;height:24px;line-height:24px;padding-left:11px;font-size:9.5px;letter-spacing:1px;color:var(--ink);text-decoration:none;border-bottom:1px solid #dedede}
.submenu a:last-child{border-bottom:none}
.banner{left:27px;top:130px;width:772px;height:312px;border:1px solid var(--line);border-radius:6px;background:linear-gradient(#fff,#eeeeee)}
.banner-art{left:45px;top:137px;width:390px;height:288px;background:linear-gradient(135deg,#f4f4f4,#c9c9c9 55%,#3a3a3a);border-radius:6px;opacity:.85}
.banner-title{left:503px;top:216px;font-family:Oswald,sans-serif;font-weight:500;font-size:34px;letter-spacing:2px;color:var(--orange)}
.banner-copy{left:503px;top:257px;font-family:Oswald,sans-serif;font-size:16px;line-height:24px;letter-spacing:1.9px;color:#2b2f33}
.dots{left:692px;top:415px;display:flex;gap:6px}
.dots span{width:12px;height:12px;border-radius:50%;background:var(--dark)}
.dots span:first-child{background:var(--orange)}
.section-title{font-family:Oswald,sans-serif;font-weight:500;font-size:16px;color:var(--ink)}
.products{left:29px;top:496px;width:766px;height:171px;border:1px solid var(--line);border-radius:6px}
.product{position:absolute;top:8px;width:110px;text-align:center;font-size:10.5px}
.product-img{height:115px;margin:0 22px;border-radius:6px;background:linear-gradient(160deg,#3a3a3a,#888 55%,#e2e2e2)}
.product-brand{margin-top:12px;color:var(--orange)}
.product-name{margin-top:3px;color:#222}
.video{left:30px;top:693px;width:303px;height:209px;background:#000}
.video-art{left:78px;top:14px;width:146px;height:160px;background:linear-gradient(#d8d8d8,#8a8a8a);border-radius:12px;opacity:.8}
.player{left:0;bottom:0;width:303px;height:17px;background:linear-gradient(#e4e4e4,#b8b8b8)}
.feature{left:378px;width:416px;height:69px;border:1px solid var(--line);background:linear-gradient(#fff,#f5f5f5)}
.feature-icon{left:14px;top:18px;width:30px;height:32px;border-radius:6px;background:linear-gradient(#f5b54a,#4a8fd6)}
.feature h3{position:absolute;left:60px;top:13px;font-family:Oswald,sans-serif;font-weight:400;font-size:11.5px;color:var(--orange)}
.feature p{position:absolute;left:62px;top:32px;width:345px;font-size:10.2px;line-height:16px;color:var(--muted)}
.info{left:0;top:922px;width:819px;height:212px;background:var(--panel);border-top:1px solid #e4e4e4}
.col{position:absolute;top:17px;width:222px}
.col h2{font-family:Oswald,sans-serif;font-weight:400;font-size:16px;color:var(--ink);margin-bottom:6px}
.col p{font-size:10.2px;line-height:16px;text-align:justify;color:var(--muted)}
.col ul{list-style:none;margin-top:-1px}
.col li{font-size:10.2px;line-height:18.3px;color:var(--orange);padding-left:13px;position:relative}
.col li::before{content:"";position:absolute;left:2px;top:8px;width:4px;height:4px;border-radius:50%;background:#999}
.footer{left:0;top:1164px;width:819px;height:36px;background:var(--dark);color:#fff;font-size:9.5px;padding:14px 0 0 28px}
</style>
</head>
<body>
<div class="page">
  <div class="abs topbar"></div>
  <div class="abs lang-label">Select Language</div>
  <svg class="abs flag flag-us" viewBox="0 0 37 22" aria-label="English">
    <rect width="37" height="22" fill="#fff"/>
    <g fill="#c8102e"><rect y="0" width="37" height="2"/><rect y="4" width="37" height="2"/><rect y="8" width="37" height="2"/><rect y="12" width="37" height="2"/><rect y="16" width="37" height="2"/><rect y="20" width="37" height="2"/></g>
    <rect width="16" height="12" fill="#1f2a6b"/>
  </svg>
  <svg class="abs flag flag-tr" viewBox="0 0 37 22" aria-label="Türkçe">
    <rect width="37" height="22" fill="#e30a17"/>
    <circle cx="14" cy="11" r="6.5" fill="#fff"/>
    <circle cx="15.8" cy="11" r="5.2" fill="#e30a17"/>
    <polygon points="22,11 25.5,9.8 25.5,8 27.2,10.5 30.5,9.8 28.3,11 30.5,12.2 27.2,11.5 25.5,14 25.5,12.2" fill="#fff"/>
  </svg>

  <div class="abs brand"><span class="brand-mark"></span>DURVELO</div>

  <nav class="abs nav">
    <a href="#" style="width:106px">HOT PRODUCTS</a>
    <a href="#" style="width:145px">SCREEN PROTECTORS</a>
    <a href="#" style="width:64px">VIDEOS</a>
    <a href="#" style="width:105px">CONTACT US</a>
  </nav>

  <div class="abs banner"></div>
  <div class="abs banner-art" role="img" aria-label="Smartphone with a clear screen protector film beside it"></div>
  <div class="abs submenu">
    <a href="#">HOT PRODUCTS</a>
    <a href="#">SCREEN PROTECTORS</a>
    <a href="#">VIDEOS</a>
    <a href="#">CONTACT US</a>
  </div>
  <div class="abs banner-title">PROTECT</div>
  <div class="abs banner-copy">GET THE AWARD WINNING<br>PROTECTION OF THE CLEARGUARD<br>THE ORIGINAL AND INDUSTRY...</div>
  <div class="abs dots"><span></span><span></span><span></span><span></span></div>

  <div class="abs section-title" style="left:34px;top:464px">NEW PRODUCTS</div>
  <div class="abs products">
    <div class="product" style="left:18px"><div class="product-img" role="img" aria-label="Phone with screen protector"></div><div class="product-brand">NORVAK</div><div class="product-name">C1 Protect</div></div>
    <div class="product" style="left:141px"><div class="product-img" role="img" aria-label="Phone with screen protector"></div><div class="product-brand">NORVAK</div><div class="product-name">C1 Protect</div></div>
    <div class="product" style="left:282px"><div class="product-img" role="img" aria-label="Phone with screen protector"></div><div class="product-brand">NORVAK</div><div class="product-name">C1 Protect</div></div>
    <div class="product" style="left:412px"><div class="product-img" role="img" aria-label="Keyboard phone with screen protector"></div><div class="product-brand">NORVAK</div><div class="product-name">C1 Protect</div></div>
    <div class="product" style="left:550px"><div class="product-img" role="img" aria-label="Phone with screen protector"></div><div class="product-brand">NORVAK</div><div class="product-name">C1 Protect</div></div>
    <div class="product" style="left:654px"><div class="product-img" role="img" aria-label="Phone with screen protector"></div><div class="product-brand">NORVAK</div><div class="product-name">C1 Protect</div></div>
  </div>

  <div class="abs video">
    <div class="abs video-art" role="img" aria-label="Video frame showing a phone outline with protector film"></div>
    <div class="abs player">
      <svg width="303" height="17" viewBox="0 0 303 17">
        <polygon points="9,4 9,13 17,8.5" fill="#222"/>
        <rect x="24" y="6" width="4" height="5" fill="#333"/><polygon points="28,6 32,3 32,14 28,11" fill="#333"/>
        <text x="42" y="12" font-size="7" fill="#222" font-family="Arial, sans-serif">3:12 / 3:12</text>
        <rect x="85" y="7" width="178" height="3" fill="#d5262b"/>
        <circle cx="263" cy="8.5" r="4" fill="#eee" stroke="#555"/>
        <rect x="274" y="4" width="9" height="9" fill="none" stroke="#333"/>
        <rect x="288" y="4" width="11" height="9" rx="2" fill="#333"/>
      </svg>
    </div>
  </div>

  <div class="abs feature" style="top:691px">
    <div class="abs feature-icon" role="img" aria-label="Pen over a screen icon"></div>
    <h3>ANTI SCRATCH</h3>
    <p>Lorem Ipsum is simply dummy text of the printing and typesetting industry. Lorem Ipsum has been the industry's standard dummy text...</p>
  </div>
  <div class="abs feature" style="top:763px">
    <div class="abs feature-icon" role="img" aria-label="Pointing finger icon"></div>
    <h3>ANTI FINGER PRINT</h3>
    <p>Lorem Ipsum is simply dummy text of the printing and typesetting industry. Lorem Ipsum has been the industry's standard dummy text...</p>
  </div>
  <div class="abs feature" style="top:835px">
    <div class="abs feature-icon" role="img" aria-label="Folder with phone icon"></div>
    <h3>WASHABLE</h3>
    <p>Lorem Ipsum is simply dummy text of the printing and typesetting industry. Lorem Ipsum has been the industry's standard dummy text...</p>
  </div>

  <section class="abs info">
    <div class="col" style="left:31px">
      <h2>WELCOME</h2>
      <p>Lorem Ipsum is simply dummy text of the printing and typesetting industry. Lorem Ipsum has been the industry's standard dummy text ever since the 1500s, when an unknown printer took a galley of type and scrambled it to make a type specimen book. It has survived not only five centuries, but also the leap into electronic typesetting, remaining essentially unchanged. It was popularised in the 1960s with the release of Kalvex sheets containing Lorem Ipsum</p>
    </div>
    <div class="col" style="left:318px">
      <h2>ABOUT US</h2>
      <p>Lorem Ipsum is simply dummy text of the printing and typesetting industry. Lorem Ipsum has been the industry's standard dummy text ever since the 1500s, when an unknown printer took a galley of type and scrambled it to make a type specimen book. It has survived not only five centuries, but also the leap into electronic typesetting, remaining essentially unchanged. It was popularised in the 1960s with the release of Kalvex sheets containing Lorem Ipsum</p>
    </div>
    <div class="col" style="left:590px">
      <h2 style="margin-left:8px">OUR SERVICES</h2>
      <ul>
        <li>Lorem Ipsum is simply dummy text of</li>
        <li>Lorem Ipsum is simply dummy</li>
        <li>Lorem Ipsum is simply dummy text of</li>
        <li>Lorem Ipsum is simply dummy text</li>
        <li>Lorem Ipsum is simply dummy text of</li>
        <li>Lorem Ipsum is simply dummy</li>
        <li>Lorem Ipsum is simply dummy text of</li>
        <li>Lorem Ipsum is simply dummy text of</li>
      </ul>
    </div>
  </section>

  <footer class="abs footer">© 2013 &nbsp;|&nbsp; PRIVACY POLICY</footer>
</div>
</body>
</html>
```